Business card for hedge fund
Vornelle Capital Management
Project: Business card for hedge fund
Business card for hedge fund - Financial Services
Creative Brief
Professional
Wanrudee Halvorsen
Chief Operating Officer
wanru.halvorsen@vornellecap.example
2 additional names: Martin Gaskell, Portfolio Manager p: +1-555-382-4719 e-mail: martin.gaskell@vornellecap.example Jia Luo, Portfolio Manager p: +852-5123-9046 e: jia.luo@vornellecap.example No address to be included

```html
<!DOCTYPE html>
<html lang="en">
<head>
<meta charset="utf-8">
<title>Vornelle Capital Management – Business Card</title>
<link href="https://fonts.googleapis.com/css2?family=Cinzel:wght@400&family=Open+Sans:wght@400;700&display=swap" rel="stylesheet">
<style>
  :root {
    --backdrop: #e9e6e1;
    --card: #ffffff;
    --ink: #2f2f2f;
    --ink-soft: #555555;
    --charcoal: #3d3d3f;
    --amber: #f6a623;
    --amber-deep: #e2830b;
  }
  * { box-sizing: border-box; margin: 0; padding: 0; }
  html, body {
    width: 1200px; height: 914px; overflow: hidden;
    background: var(--backdrop);
  }
  .canvas {
    position: relative; width: 1200px; height: 914px;
    display: flex; align-items: center; justify-content: center;
  }
  .card {
    position: relative; width: 1000px; height: 572px;
    background: var(--card);
    box-shadow: 0 10px 30px rgba(0,0,0,0.12);
    overflow: hidden;
  }
  .card__swoosh { position: absolute; inset: 0; width: 100%; height: 100%; }
  .brand {
    position: absolute; left: 70px; top: 92px;
    font-family: "Cinzel", serif; font-weight: 400; color: var(--ink);
    display: flex; align-items: center; gap: 18px;
  }
  .brand__mark {
    width: 22px; height: 22px; border-radius: 50%; background: var(--ink);
  }
  .brand__name { font-size: 58px; line-height: 1; letter-spacing: 3px; }
  .brand__sub { font-size: 19px; letter-spacing: 3px; margin-top: 8px; }
  .contacts {
    position: absolute; left: 66px; top: 236px;
    list-style: none;
    font-family: "Open Sans", sans-serif; font-size: 17px; color: var(--ink-soft);
  }
  .contacts__item { display: flex; align-items: center; gap: 14px; height: 32px; }
  .contacts__icon { width: 24px; height: 24px; flex: none; }
  .holder {
    position: absolute; right: 56px; bottom: 44px; text-align: left;
    font-family: "Open Sans", sans-serif; color: var(--ink);
  }
  .holder__name { font-size: 20px; font-weight: 700; }
  .holder__role { font-size: 15px; color: var(--ink-soft); margin-top: 2px; }
</style>
</head>
<body>
<main class="canvas">
  <article class="card">
    <svg class="card__swoosh" viewBox="0 0 1000 572" aria-hidden="true">
      <defs>
        <linearGradient id="amberBand" x1="0" y1="0" x2="1" y2="1">
          <stop offset="0" stop-color="var(--amber)"/>
          <stop offset="1" stop-color="var(--amber-deep)"/>
        </linearGradient>
      </defs>
      <path d="M700,0 C830,60 945,170 1000,330 L1000,0 Z" fill="var(--charcoal)"/>
      <path d="M640,0 C810,70 950,210 1000,400 L1000,330 C945,170 830,60 700,0 Z" fill="url(#amberBand)"/>
      <path d="M800,0 C880,60 950,140 1000,240 L1000,210 C955,130 890,55 830,0 Z" fill="url(#amberBand)"/>
    </svg>

    <header class="brand">
      <span class="brand__mark"></span>
      <div>
        <div class="brand__name">VORNELLE</div>
        <div class="brand__sub">CAPITAL MANAGEMENT</div>
      </div>
    </header>

    <ul class="contacts">
      <li class="contacts__item">
        <svg class="contacts__icon" viewBox="0 0 24 24"><circle cx="12" cy="12" r="12" fill="var(--charcoal)"/><path d="M8.5 6.5l2 2-1.2 1.5a7 7 0 0 0 4.7 4.7l1.5-1.2 2 2-1.3 1.8C11.6 17.3 6.7 12.4 6.7 7.8z" fill="#fff"/></svg>
        <span>+1-555-214-8830</span>
      </li>
      <li class="contacts__item">
        <svg class="contacts__icon" viewBox="0 0 24 24"><circle cx="12" cy="12" r="12" fill="var(--charcoal)"/><rect x="8.5" y="5.5" width="7" height="13" rx="1.2" fill="#fff"/><rect x="9.7" y="7.2" width="4.6" height="8" fill="var(--charcoal)"/></svg>
        <span>+1-555-467-1092</span>
      </li>
      <li class="contacts__item">
        <svg class="contacts__icon" viewBox="0 0 24 24"><circle cx="12" cy="12" r="12" fill="var(--charcoal)"/><rect x="6" y="10" width="12" height="7" rx="1" fill="#fff"/><rect x="8.5" y="6" width="7" height="5" fill="#fff"/></svg>
        <span>+1-555-903-5561</span>
      </li>
      <li class="contacts__item">
        <svg class="contacts__icon" viewBox="0 0 24 24"><circle cx="12" cy="12" r="12" fill="var(--charcoal)"/><rect x="6" y="8" width="12" height="8.5" rx="1" fill="#fff"/><path d="M6.5 8.5l5.5 4.5 5.5-4.5" fill="none" stroke="var(--charcoal)" stroke-width="1.3"/></svg>
        <span>wanru.halvorsen@vornellecap.example</span>
      </li>
      <li class="contacts__item">
        <svg class="contacts__icon" viewBox="0 0 24 24"><circle cx="12" cy="12" r="12" fill="var(--charcoal)"/><g fill="none" stroke="#fff" stroke-width="1.3"><circle cx="12" cy="12" r="6"/><ellipse cx="12" cy="12" rx="2.6" ry="6"/><path d="M6 12h12"/></g></svg>
        <span>www.vornellecap.example</span>
      </li>
    </ul>

    <footer class="holder">
      <div class="holder__name">Wanrudee Halvorsen</div>
      <div class="holder__role">Chief Operating Officer</div>
    </footer>
  </article>
</main>
</body>
</html>
```